International emerging specialist Research and Development Company focused on plant-based medicine

We need a powerpoint design for a new company based in British Columbia, Canada called Valtio Pharmex. We are focused on developing plant-based medicines. The company is driven by its experience in research and development work in plant genetics, cultivation techniques, natural medicines, biochemistry, agriculture and technologies. Valtio will research, develop and produce very unique and specific cultivars from the plant kingdom needed for specific ailments in medical patients. We would like to see designs that use our current logo and its colour scheme. The final design should communicate financial safety, growth, and research and development.

```html
<!DOCTYPE html>
<html lang="en">
<head>
<meta charset="utf-8">
<title>Valtio Pharmex – Project Overview</title>
<link rel="stylesheet" href="https://fonts.googleapis.com/css2?family=Roboto:wght@400;700&family=Roboto+Condensed:wght@400&display=swap">
<style>
  :root {
    --brand-red: #d4161e;
    --page-bg: #f1f1f1;
    --footer-grey: #d4d4d4;
    --heading-grey: #7a7a7a;
    --heading-navy: #4a4c63;
    --body-text: #333333;
    --seg-crimson: #a81c24;
    --seg-red: #d42027;
    --seg-sage: #8ea3a3;
    --seg-charcoal: #3d3d3d;
    --seg-navy: #4a4c63;
    --seg-grey: #6e6e6e;
    --seg-rose: #c45a62;
    --seg-wine: #7c1520;
    --white: #ffffff;
  }
  * { margin: 0; padding: 0; box-sizing: border-box; }
  html, body { width: 1200px; height: 900px; overflow: hidden; }
  body {
    position: relative;
    background: var(--page-bg);
    font-family: "Roboto", Arial, sans-serif;
    color: var(--body-text);
  }
  .title-bar {
    position: absolute; left: 0; top: 0; width: 1200px; height: 93px;
    background: var(--brand-red);
  }
  .slide-title {
    position: absolute; left: 30px; top: 16px;
    font-family: "Roboto Condensed", "Arial Narrow", sans-serif;
    font-weight: 400; font-size: 50px; line-height: 60px;
    color: var(--white);
  }
  .brand-name {
    position: absolute; right: 18px; top: 28px;
    font-family: "Roboto", Arial, sans-serif;
    font-weight: 400; font-size: 30px; line-height: 36px;
    color: var(--white);
  }
  .footer-band {
    position: absolute; left: 0; top: 858px; width: 1200px; height: 42px;
    background: var(--footer-grey);
  }
  .cycle-diagram { position: absolute; left: 0; top: 0; width: 1200px; height: 900px; }
  .hub-name {
    position: absolute; left: 506px; top: 425px; width: 200px;
    text-align: center; font-weight: 700; font-size: 40px; line-height: 50px;
    color: var(--brand-red);
  }
  .step-number {
    position: absolute; left: 524px; top: 735px;
    font-weight: 700; font-size: 42px; line-height: 50px;
    color: var(--white);
  }
  .point { position: absolute; }
  .point-heading { font-weight: 700; font-size: 21px; line-height: 26px; }
  .point-text { font-size: 16px; line-height: 24px; margin-top: 1px; }
  .point--left .point-heading { color: var(--heading-grey); }
  .point--right .point-heading { color: var(--heading-navy); }
  .align-right { text-align: right; }
</style>
</head>
<body>
  <header class="title-bar">
    <h1 class="slide-title">Project Title Here</h1>
    <div class="brand-name">Valtio Pharmex</div>
  </header>

  <svg class="cycle-diagram" viewBox="0 0 1200 900" fill="none" stroke-width="36">
    <path d="M633.1 229.7 A222 222 0 0 1 754.5 285" stroke="var(--seg-crimson)"/>
    <path d="M780.9 313.3 A222 222 0 0 1 827.7 438.4" stroke="var(--seg-red)"/>
    <path d="M826.3 477.1 A222 222 0 0 1 771 598.5" stroke="var(--seg-sage)"/>
    <path d="M742.7 624.9 A222 222 0 0 1 617.6 671.7" stroke="var(--seg-charcoal)"/>
    <path d="M578.9 670.3 A222 222 0 0 1 457.5 615" stroke="var(--seg-navy)"/>
    <path d="M431.1 586.7 A222 222 0 0 1 384.3 461.6" stroke="var(--seg-grey)"/>
    <path d="M385.7 422.9 A222 222 0 0 1 441 301.5" stroke="var(--seg-rose)"/>
    <path d="M469.3 275.1 A222 222 0 0 1 594.4 228.3" stroke="var(--seg-wine)"/>

    <g class="connectors" stroke-width="3">
      <polyline points="758,267 810,217 930,217" stroke="var(--seg-crimson)"/>
      <polyline points="848,435 950,435" stroke="var(--seg-red)"/>
      <polyline points="795,607 848,660 938,660" stroke="var(--seg-sage)"/>
      <polyline points="446,315 368,248 292,248" stroke="var(--seg-rose)"/>
      <polyline points="372,478 292,478" stroke="var(--seg-grey)"/>
      <polyline points="458,642 402,695 292,695" stroke="var(--seg-navy)"/>
    </g>
  </svg>

  <div class="hub-name">Valtio</div>
  <div class="step-number">04</div>

  <section class="point point--left" style="left:126px; top:235px; width:230px;">
    <h2 class="point-heading">Heading Here</h2>
    <p class="point-text">Subtext here Subtext here Sub-text here Subtext here Subtext here Subtext here</p>
  </section>

  <section class="point point--left" style="left:126px; top:470px; width:230px;">
    <h2 class="point-heading">Heading Here</h2>
    <p class="point-text">Subtext here Subtext here Sub-text here Subtext here Subtext here Subtext here</p>
  </section>

  <section class="point point--left" style="left:126px; top:677px; width:170px;">
    <h2 class="point-heading">Heading Here</h2>
    <p class="point-text">Subtext here Subtext here Subtext here Sub-text here Subtext here Subtext here</p>
  </section>

  <section class="point point--right align-right" style="left:850px; top:203px; width:228px;">
    <h2 class="point-heading">Heading Here</h2>
    <p class="point-text">Subtext here Subtext here Sub-text here Subtext here Subtext here Subtext here</p>
  </section>

  <section class="point point--right align-right" style="left:862px; top:419px; width:228px;">
    <h2 class="point-heading">Heading Here</h2>
    <p class="point-text">Subtext here Subtext here Sub-text here Subtext here Subtext here Subtext here</p>
  </section>

  <section class="point point--right" style="left:855px; top:650px; width:230px;">
    <h2 class="point-heading" style="padding-left:90px;">Heading Here</h2>
    <p class="point-text">Subtext here Subtext here Sub-text here Subtext here Subtext here Subtext here</p>
  </section>

  <footer class="footer-band"></footer>
</body>
</html>
```